Breezeway Climate Business Card Design

Design new, 2 sides, business cards for a residential and light commercial heating, air conditioning contractor.

Target Market(s)

Homeowners, small businesses

Industry/Entity Type

Business

Contact Information for Business Card

Dominic Vasquerelli
Phone - 555-214-6837
Email
Address - PO box 618
Millbrook NJ 07999
Website - www.BreezewayClimateLLC.example

Requirements
Must have
• logo, company colors, standard size with no die cut, so I can use printhaven

```html
<!DOCTYPE html>
<html lang="en">
<head>
<meta charset="utf-8">
<title>Breezeway Climate – Business Card</title>
<link rel="stylesheet" href="https://fonts.googleapis.com/css2?family=Crimson+Text:ital,wght@0,400;0,600;1,400&display=swap">
<style>
  :root {
    --cream: #fdeea0;
    --crimson: #9b1f33;
    --orange: #f7941d;
    --ink: #1e1a18;
    --ring: #e8443a;
    --tagline: #f5d98a;
    --stage: #e9e6e1;
  }
  * { box-sizing: border-box; margin: 0; padding: 0; }
  html, body { width: 1200px; height: 576px; overflow: hidden; }
  body {
    background: var(--stage);
    font-family: "Crimson Text", Georgia, serif;
    color: var(--ink);
    position: relative;
  }

  /* Front side: portrait, contact details */
  .card-front {
    position: absolute;
    left: 170px; top: 34px;
    width: 290px; height: 508px;
    background: var(--cream);
    overflow: hidden;
    box-shadow: 0 4px 14px rgba(0,0,0,.18);
  }
  .card-front .edge {
    position: absolute; left: 0; top: 0; bottom: 0;
    width: 6px; background: var(--orange);
  }
  .card-front .band {
    position: absolute; left: 6px; top: 0; bottom: 0;
    width: 44px; background: var(--crimson);
  }
  .contact-row { position: absolute; left: 0; right: 0; }
  .contact-row .icon {
    position: absolute; left: 32px; top: 0;
    width: 36px; height: 36px; border-radius: 50%;
    background: var(--cream);
    border: 2px solid var(--ring);
    display: flex; align-items: center; justify-content: center;
  }
  .contact-row .icon svg { width: 16px; height: 16px; fill: var(--ink); }
  .contact-row .text {
    position: absolute; left: 80px; right: 12px; top: 7px;
    font-size: 15px; line-height: 1.2; white-space: nowrap;
  }
  .contact-row .text.small { font-size: 13px; top: 9px; }
  .name {
    color: var(--crimson);
    font-size: 17px; font-weight: 400;
    text-transform: uppercase; letter-spacing: .3px;
    line-height: 1.1;
  }
  .role { font-size: 15px; margin-top: 1px; }

  /* Back side: landscape, brand */
  .card-back {
    position: absolute;
    left: 530px; top: 143px;
    width: 508px; height: 290px;
    background: var(--crimson);
    overflow: hidden;
    box-shadow: 0 4px 14px rgba(0,0,0,.18);
  }
  .card-back .stripe {
    position: absolute; left: 0; top: 0; bottom: 0;
    width: 42px; background: var(--orange);
  }
  .brand {
    position: absolute; left: 42px; right: 0; top: 76px;
    display: flex; align-items: center; justify-content: center; gap: 12px;
  }
  .brand .mark {
    width: 28px; height: 28px; border-radius: 50%;
    background: var(--orange);
  }
  .brand .wordmark {
    color: var(--orange);
    font-size: 36px; font-weight: 600;
  }
  .tagline {
    position: absolute; left: 42px; right: 0; top: 166px;
    text-align: center;
    color: var(--tagline); font-style: italic;
    font-size: 18px; line-height: 1.3;
  }
</style>
</head>
<body>

<section class="card-front" aria-label="Business card front">
  <div class="edge"></div>
  <div class="band"></div>

  <div class="contact-row" style="top:45px">
    <div class="icon"><svg viewBox="0 0 16 16"><circle cx="8" cy="4.5" r="3.5"/><path d="M1 16c0-4 3-6.5 7-6.5s7 2.5 7 6.5z"/></svg></div>
    <div class="text" style="top:-2px">
      <div class="name">Dominic Vasquerelli</div>
      <div class="role">CEO/Founder</div>
    </div>
  </div>

  <div class="contact-row" style="top:132px">
    <div class="icon"><svg viewBox="0 0 16 16"><path d="M8 0a5.5 5.5 0 0 0-5.5 5.5C2.5 10 8 16 8 16s5.5-6 5.5-10.5A5.5 5.5 0 0 0 8 0zm0 7.8a2.3 2.3 0 1 1 0-4.6 2.3 2.3 0 0 1 0 4.6z"/></svg></div>
    <div class="text" style="top:0">PO box 618<br>Millbrook NJ 07999</div>
  </div>

  <div class="contact-row" style="top:212px">
    <div class="icon"><svg viewBox="0 0 16 16"><path d="M3.6 1l2.6 3-1.5 2a9 9 0 0 0 5 5l2-1.6 3 2.6-1.7 2.6C7 14.8 1.2 9 1 2.8z"/></svg></div>
    <div class="text">(555) 214-6837</div>
  </div>

  <div class="contact-row" style="top:281px">
    <div class="icon"><svg viewBox="0 0 16 16"><path d="M3 1h10v14H3zm1.6 1.6v10.8h6.8V2.6z"/></svg></div>
    <div class="text">(555) 214-6838</div>
  </div>

  <div class="contact-row" style="top:350px">
    <div class="icon"><svg viewBox="0 0 16 16"><path d="M1 3h14v10H1zm1.5 1.3v.4L8 8.8l5.5-4.1v-.4zm0 2.2v5.2h11V6.5L8 10.6z"/></svg></div>
    <div class="text small">dominic@breezewayclimate.example</div>
  </div>

  <div class="contact-row" style="top:421px">
    <div class="icon"><svg viewBox="0 0 16 16"><circle cx="8" cy="8" r="7"/><path d="M5 4c2 0 2 2 4 2s0 3-2 3-1 3-3 2-2-5 1-7z" fill="#fdeea0"/></svg></div>
    <div class="text small">www.BreezewayClimateLLC.example</div>
  </div>
</section>

<section class="card-back" aria-label="Business card back">
  <div class="stripe"></div>
  <div class="brand">
    <span class="mark"></span>
    <span class="wordmark">Breezeway Climate</span>
  </div>
  <p class="tagline">Residential &amp; Light Commercial Heating<br>Air conditioning</p>
</section>

</body>
</html>
```